Web Design Project

We need to have you design a 7 page design for ecommerce site.

The design will consist of a Home Page, Category Landing Page, Category Product Page, Product Page, Cart Page, Gift Registry Page, and Virtual Place Setting Page

The goal will be a design which is similar to:

http://www.pellorin.example/ in terms of layout of the home page

http://www.pellorin.example/decor The category landing pages will look a bit like this

http://www.pellorin.example/decor/decorative-pillows. The category product pages will look like this , however, will have more of a layered navigation on the left where you can sort by brand, price, finish, etc. instead of ability to shop by category here

http://www.pellorin.example/p/velmora-dinnerware The product page can be similar to this one

Please add a product to cart as the cart page can be very similar to the look and feel here.

For the gift registry landing page, here are some examples: http://www.hollowcrestgoods.example/regHome.asp

http://www.ferrant-dalby.example/registry/

Last, we need to create a virtual place setting app like this: http://www.luminacasa.example/style-your-table

But more better and stylish, mapping in with the theme.

Industry/Entity Type

Shop

Requirements
Must have
• - This needs to have a sophisticated, luxurious look and feel. Please make sure to design a 'showcase' style page for the main categorly landing pages.

```html
<!DOCTYPE html>
<html lang="en">
<head>
<meta charset="utf-8">
<title>Marwick &amp; Vale — Home</title>
<link href="https://fonts.googleapis.com/css2?family=PT+Sans:wght@400;700&family=PT+Sans+Narrow:wght@400;700&family=Oswald:wght@500&display=swap" rel="stylesheet">
<style>
:root{
  --page:#ffffff;
  --backdrop:#f4f4f4;
  --rule:#a7a7a2;
  --nav-top:#5e7a4c;
  --nav-bottom:#3d5530;
  --nav-divider:#8aa27a;
  --ink:#3a3a3a;
  --muted:#6d6d6d;
  --accent:#ef6a15;
  --footer:#d2e1b8;
  --footer-rule:#a8b894;
  --btn-dark:#1f1f1f;
  --btn-green:#536b45;
  --util-bg:#ededed;
  --brand-dot:#8ea97b;
}
*{box-sizing:border-box;margin:0;padding:0}
html,body{width:1106px;height:1200px;overflow:hidden;background:var(--backdrop)}
body{font-family:"PT Sans",Arial,sans-serif;color:var(--ink);position:relative}
.page{position:absolute;left:27px;top:0;width:1054px;height:1200px;background:var(--page);border-top:3px solid var(--rule)}
.abs{position:absolute}
/* header */
.brand{left:40px;top:58px;display:flex;align-items:center;gap:10px}
.brand-dot{width:14px;height:14px;border-radius:50%;background:var(--brand-dot)}
.brand-name{font-family:"PT Sans",sans-serif;font-weight:400;font-size:24px;color:#4a4a4a;white-space:nowrap}
.utility{left:663px;top:2px;width:373px;height:44px;background:var(--util-bg);border-radius:0 0 6px 6px;display:flex;align-items:center;justify-content:space-around;padding:0 10px;font-size:13px;color:#444}
.utility span{display:flex;align-items:center;gap:5px}
.utility svg{width:18px;height:18px;fill:#666}
.search{left:718px;top:96px;width:319px;height:30px;display:flex}
.search input{flex:1;border:1px solid #cfcfcf;font:italic 12px "PT Sans",sans-serif;padding:0 12px;color:#777}
.search button{width:79px;background:var(--btn-dark);color:#fff;border:0;font:700 13px "PT Sans",sans-serif;letter-spacing:.5px}
.nav{left:0;top:145px;width:1054px;height:51px;background:linear-gradient(var(--nav-top),var(--nav-bottom));display:flex}
.nav a{color:#fff;text-decoration:none;font-size:15px;display:flex;align-items:center;justify-content:center;border-right:1px solid var(--nav-divider);text-transform:uppercase}
.nav a:last-child{border-right:0}
/* hero */
.hero{left:12px;top:213px;width:694px;height:395px;background:linear-gradient(90deg,#b98a55 0 22%,#e8e2d6 22% 70%,#d8d2c6 70%)}
.hero-bar{position:absolute;left:0;bottom:0;width:100%;height:28px;background:rgba(60,60,60,.55);display:flex;justify-content:center;align-items:center;gap:5px}
.hero-bar i{width:9px;height:9px;border-radius:50%;background:#fff}
.tile{left:715px;width:326px;height:194px}
.tile-dinner{top:213px;background:linear-gradient(135deg,#c9a0b4,#d9c6b3 60%,#b99680)}
.tile-table{top:413px;background:linear-gradient(135deg,#8a3a20,#c97b52 55%,#e6d2b8)}
.tile-caption{position:absolute;left:0;bottom:0;width:100%;height:42px;background:rgba(50,40,35,.6);display:flex;align-items:center;justify-content:space-between;padding:0 25px 0 18px}
.tile-caption h2{font-family:"Oswald",sans-serif;font-weight:500;font-size:21px;color:#fff;text-transform:uppercase}
.tile-caption span{background:#fff;font:700 11px "PT Sans Narrow",sans-serif;padding:6px 12px;border-radius:3px;color:#222;text-transform:uppercase}
/* promo cards */
.card{top:636px;width:333px;height:194px;border:1px solid #e0e0e0;display:flex;overflow:hidden}
.card-body{width:175px;padding:18px 0 0 20px}
.card h3{font-family:"PT Sans Narrow",sans-serif;font-weight:700;font-size:23px;line-height:28px;color:var(--accent);margin-bottom:8px}
.card p{width:142px;font-size:11px;line-height:18px;color:var(--muted)}
.card .more{display:inline-block;margin-top:13px;background:#f1f1f1;color:var(--accent);font:700 14px "PT Sans Narrow",sans-serif;padding:5px 10px;text-transform:uppercase}
.card-photo{flex:1}
/* footer */
.footer{left:0;top:866px;width:1054px;height:264px;background:var(--footer);border-top:3px solid #6e6e6a}
.col{position:absolute;top:36px}
.col h4{font-weight:400;font-size:15px;text-transform:uppercase;color:#333;margin-bottom:14px}
.col li{list-style:none;font-size:12.5px;line-height:24px;color:#444}
.vrule{position:absolute;top:34px;width:1px;height:200px;background:var(--footer-rule)}
.news p{font-size:11.5px;margin-bottom:8px}
.news input{width:216px;height:30px;border:1px solid #b5c3a2;font:italic 11px "PT Sans",sans-serif;padding:0 12px}
.news button{display:block;margin:6px 0 0 141px;background:var(--btn-green);color:#fff;border:0;border-radius:3px;font:12px "PT Sans",sans-serif;padding:5px 13px}
.social{display:flex;align-items:center;gap:4px;margin-top:22px;font-size:12px}
.social span{margin-right:9px}
.social i{width:24px;height:24px;border-radius:50%;background:#222}
.legal{left:0;top:1148px;width:1054px;text-align:center;font-size:12.5px;color:#444}
</style>
</head>
<body>
<div class="page">
  <div class="abs brand"><div class="brand-dot"></div><div class="brand-name">Marwick &amp; Vale</div></div>

  <div class="abs utility">
    <span><svg viewBox="0 0 20 20"><path d="M1 3h3l2 9h10l2-7H6" fill="none" stroke="#666" stroke-width="2"/><circle cx="8" cy="16" r="2"/><circle cx="15" cy="16" r="2"/></svg>My Cart</span>
    <span><svg viewBox="0 0 20 20"><rect x="4" y="9" width="12" height="10" rx="1"/><path d="M7 9V6a3 3 0 0 1 6 0v3" fill="none" stroke="#666" stroke-width="2"/></svg>Log In</span>
    <span><svg viewBox="0 0 20 20"><circle cx="10" cy="6" r="4"/><path d="M2 19c0-5 4-7 8-7s8 2 8 7z"/></svg>My Account</span>
    <span><svg viewBox="0 0 20 20"><rect x="1" y="9" width="4" height="10"/><path d="M7 9l4-7c2 0 2 2 2 3l-1 3h6c1 0 2 1 1 3l-2 7H7z"/></svg>Sign Up</span>
  </div>

  <form class="abs search"><input type="text" value="Search here.."><button type="button">SEARCH</button></form>

  <nav class="abs nav">
    <a style="width:92px">Home</a><a style="width:108px">About Us</a><a style="width:130px">Store Events</a><a style="width:92px">Orders</a><a style="width:116px">Products</a><a style="width:158px">Corporate Sales</a><a style="width:100px">On Sale</a><a style="width:101px">Support</a><a style="flex:1">Contact Us</a>
  </nav>

  <div class="abs hero" role="img" aria-label="Study room with wooden desk, chair, bookshelf and daybed">
    <div class="hero-bar"><i></i><i></i><i></i><i></i></div>
  </div>
  <div class="abs tile tile-dinner" role="img" aria-label="Patterned ceramic dinner bowls">
    <div class="tile-caption"><h2>Modern Dinner Set</h2><span>View More</span></div>
  </div>
  <div class="abs tile tile-table" role="img" aria-label="Wooden dining table with chairs">
    <div class="tile-caption"><h2>Dinning Table</h2><span>View More</span></div>
  </div>

  <div class="abs card" style="left:12px">
    <div class="card-body"><h3>Best Products</h3><p>Pellentesque habitant morbi tristique senectus et netus et malesuada fames ac turpis egestas. posuere felis nec tortor.</p><span class="more">View More</span></div>
    <div class="card-photo" role="img" aria-label="Green ceramic lidded bowl" style="background:linear-gradient(135deg,#f2f2ee,#dfe3da 50%,#4f6f45)"></div>
  </div>
  <div class="abs card" style="left:359px">
    <div class="card-body"><h3>Featured Product</h3><p>Pellentesque habitant morbi tristique senectus et netus et malesuada fames ac turpis egestas. posuere felis nec tortor.</p><span class="more">View More</span></div>
    <div class="card-photo" role="img" aria-label="Assorted kitchen utensils and cookware" style="background:linear-gradient(135deg,#f4f4f4,#9a9a9a 50%,#3a3a3a)"></div>
  </div>
  <div class="abs card" style="left:705px">
    <div class="card-body"><h3>Wedding Specials</h3><p>Pellentesque habitant morbi tristique senectus et netus et malesuada fames ac turpis egestas. posuere felis nec tortor.</p><span class="more">View More</span></div>
    <div class="card-photo" role="img" aria-label="Wrapped wedding gift boxes with ribbon" style="background:linear-gradient(135deg,#dfe6f0,#f4f6fa 50%,#c9d2de)"></div>
  </div>

  <footer class="abs footer">
    <div class="col news" style="left:32px;top:40px">
      <h4>Newsletters Sign Up</h4>
      <p>Please Sign up here for latest Newsletters</p>
      <input type="text" value="email address here">
      <button type="button">Subscribe</button>
      <div class="social"><span>Connect With Us on</span><i></i><i></i><i></i><i></i></div>
    </div>
    <div class="vrule" style="left:292px"></div>
    <div class="col" style="left:321px"><h4>Online Shopping</h4><ul><li>Shopping Itmes</li><li>My Cart</li><li>Wish List</li><li>Shopping Cart</li><li>On Sales</li><li>Member</li></ul></div>
    <div class="vrule" style="left:475px"></div>
    <div class="col" style="left:503px"><h4>Our Products</h4><ul><li>Artist/Manufacturer</li><li>Barware</li><li>Dinnerware</li><li>Stemware/Drinkware</li><li>Flatware</li><li>Linens &amp; Placemats</li></ul></div>
    <div class="vrule" style="left:659px"></div>
    <div class="col" style="left:698px"><h4>About</h4><ul><li>Why We Are</li><li>Specials</li><li>Latest Itmes</li><li>Special Offers</li><li>Location</li><li>Categories</li></ul></div>
    <div class="vrule" style="left:846px"></div>
    <div class="col" style="left:885px"><h4>Support</h4><ul><li>FAQ</li><li>Shop Now</li><li>Locations</li><li>Customer Support</li><li>Contact Us</li></ul></div>
  </footer>

  <div class="abs legal">© 2012 Company Name.&nbsp; All right reserved.&nbsp; Privacy/Terms and Conditions</div>
</div>
</body>
</html>
```